2021 Summer Ads Danford Vale Custom Homes

We need a re-design of our summer ad run for our customer, Danford Vale Custom Homes. They are custom home builders in the mostly rural parts of West Virginia, USA. They are known for their "Forever Home" tagline. We'd like two designed ads with the main difference being just the custom home that's featured. These designs should be for a Google banner like 300 x 250 and square ad like 250 x 250. For inspiration please visit the Danford Vale Custom Homes website at www dot danfordvalecustomhomes dot com

Target Market(s)

consumers / new home shoppers

Industry/Entity Type

Consumer

Requirements
Must have
• DVCH logo
Price Lock Available!
Custom home pic
Learn more >
small TBWG logo mark

```html
<!DOCTYPE html>
<html lang="en">
<head>
<meta charset="utf-8">
<title>Danford Vale Custom Homes – Summer Banners</title>
<link rel="stylesheet" href="https://fonts.googleapis.com/css2?family=Montserrat:wght@300;400;600;700;800&display=swap">
<style>
  :root {
    --page-bg: #d7d8d9;
    --ink-dark: #1d1d25;
    --ink-navy: #141a33;
    --brand-red: #e0192f;
    --brand-red-deep: #8e0c1d;
    --brand-red-mid: #b5111f;
    --white: #ffffff;
    --dusk-top: #6f7aa8;
    --dusk-bottom: #3a3448;
    --day-top: #9fc0dc;
    --day-bottom: #dfe3e0;
  }
  * { box-sizing: border-box; margin: 0; padding: 0; }
  html, body {
    width: 1200px;
    height: 894px;
    overflow: hidden;
    background: var(--page-bg);
    font-family: "Montserrat", Arial, sans-serif;
  }
  .banner {
    position: absolute;
    left: 90px;
    width: 997px;
    height: 333px;
    overflow: hidden;
    color: var(--white);
  }
  .banner--dusk { top: 101px; background: var(--ink-dark); }
  .banner--day  { top: 484px; background: var(--brand-red-deep); }

  .banner__photo { position: absolute; top: 0; right: 0; height: 100%; }
  .banner--dusk .banner__photo {
    width: 600px;
    background:
      radial-gradient(ellipse at 60% 75%, rgba(255,214,150,.55), transparent 45%),
      linear-gradient(180deg, var(--dusk-top) 0%, #a99bb0 35%, #f2f0ec 55%, #6b5f5a 80%, var(--dusk-bottom) 100%);
  }
  .banner--day .banner__photo {
    width: 560px;
    background:
      radial-gradient(ellipse at 55% 65%, #f4f4f2 0%, #e6e7e5 35%, transparent 60%),
      linear-gradient(180deg, var(--day-top) 0%, #c9d6de 30%, var(--day-bottom) 60%, #5f7350 100%);
  }
  .banner__shapes { position: absolute; inset: 0; width: 100%; height: 100%; }

  .banner__logo {
    position: absolute;
    left: 50px;
    top: 22px;
    font-weight: 700;
    font-size: 30px;
    letter-spacing: 2px;
    text-transform: uppercase;
  }
  .banner__headline {
    position: absolute;
    left: 48px;
    top: 88px;
    text-transform: uppercase;
    line-height: 1.0;
  }
  .headline__lead { display: block; font-weight: 400; font-size: 38px; margin-bottom: 5px; }
  .headline__main { display: block; font-weight: 700; font-size: 41px; line-height: 1.0; }
  .banner__offer {
    position: absolute;
    left: 50px;
    top: 222px;
    font-weight: 700;
    font-size: 20px;
    text-transform: uppercase;
  }
  .banner--day .banner__offer { top: 226px; }

  .cta {
    position: absolute;
    left: 48px;
    top: 264px;
    width: 180px;
    height: 50px;
    display: flex;
    text-decoration: none;
    color: var(--white);
  }
  .cta__label {
    flex: 1;
    display: flex;
    align-items: center;
    justify-content: center;
    font-weight: 700;
    font-size: 16px;
    text-transform: uppercase;
    border-radius: 3px 0 0 3px;
  }
  .cta__tab {
    width: 34px;
    display: flex;
    align-items: center;
    justify-content: center;
    clip-path: polygon(0 0, 80% 0, 100% 50%, 80% 100%, 0 100%);
  }
  .banner--dusk .cta__label { background: var(--brand-red); }
  .banner--dusk .cta__tab { background: #8d0f1c; }
  .banner--day .cta { top: 262px; }
  .banner--day .cta__label { background: var(--ink-navy); }
  .banner--day .cta__tab { background: var(--brand-red); }

  .partner {
    position: absolute;
    left: 268px;
    top: 270px;
    display: flex;
    align-items: center;
    gap: 8px;
    font-weight: 700;
    font-size: 30px;
  }
  .partner__mark { width: 14px; height: 14px; background: var(--white); }
  .banner--day .partner { left: 300px; top: 262px; }
</style>
</head>
<body>

<section class="banner banner--dusk">
  <div class="banner__photo" role="img" aria-label="Photo of a white two-storey custom home with a blue metal roof and lit wraparound screened porch at dusk"></div>
  <svg class="banner__shapes" viewBox="0 0 600 200" preserveAspectRatio="none" aria-hidden="true">
    <defs>
      <linearGradient id="stripe-red" x1="0" y1="0" x2="0" y2="1">
        <stop offset="0" stop-color="#ff2a3f"/>
        <stop offset="1" stop-color="#a00d1c"/>
      </linearGradient>
    </defs>
    <polygon points="0,0 332,0 272,200 0,200" fill="#1d1d25"/>
    <polygon points="0,0 40,0 0,30" fill="#b0101f"/>
    <polygon points="0,200 0,175 30,200" fill="#7e0c19"/>
    <polygon points="290,0 318,0 258,200 232,200" fill="#2a2a33"/>
    <polygon points="318,0 344,0 284,200 262,200" fill="url(#stripe-red)"/>
    <rect x="270" y="194" width="330" height="6" fill="#e0192f"/>
  </svg>
  <div class="banner__logo">Danford Vale</div>
  <h2 class="banner__headline">
    <span class="headline__lead">Start Building</span>
    <span class="headline__main">Your Forever<br>Home Today!</span>
  </h2>
  <p class="banner__offer">Price Lock Available!</p>
  <a class="cta" href="#">
    <span class="cta__label">Learn More</span>
    <span class="cta__tab">
      <svg width="12" height="16" viewBox="0 0 12 16" aria-hidden="true"><path d="M2 2 L9 8 L2 14" fill="none" stroke="#fff" stroke-width="3"/></svg>
    </span>
  </a>
  <div class="partner"><span class="partner__mark"></span>TBWG</div>
</section>

<section class="banner banner--day">
  <div class="banner__photo" role="img" aria-label="Rendering of a white board-and-batten cottage with a silver standing-seam roof, dormer and wooden front door"></div>
  <svg class="banner__shapes" viewBox="0 0 600 200" preserveAspectRatio="none" aria-hidden="true">
    <defs>
      <linearGradient id="panel-red" x1="0" y1="0" x2="1" y2="1">
        <stop offset="0" stop-color="#7a0a18"/>
        <stop offset="0.6" stop-color="#a40f20"/>
        <stop offset="1" stop-color="#d3162b"/>
      </linearGradient>
    </defs>
    <path d="M0 0 H262 Q352 50 336 200 H0 Z" fill="url(#panel-red)"/>
    <path d="M262 0 Q352 50 336 200" fill="none" stroke="#fff" stroke-width="7"/>
    <path d="M274 0 Q364 52 346 200" fill="none" stroke="#b3111f" stroke-width="3"/>
  </svg>
  <div class="banner__logo">Danford Vale</div>
  <h2 class="banner__headline">
    <span class="headline__lead">Start Building</span>
    <span class="headline__main">Your Forever<br>Home Today!</span>
  </h2>
  <p class="banner__offer">Price Lock Available!</p>
  <a class="cta" href="#">
    <span class="cta__label">Learn More</span>
    <span class="cta__tab">
      <svg width="12" height="16" viewBox="0 0 12 16" aria-hidden="true"><path d="M2 2 L9 8 L2 14" fill="none" stroke="#fff" stroke-width="3"/></svg>
    </span>
  </a>
  <div class="partner"><span class="partner__mark"></span>TBWG</div>
</section>

</body>
</html>
```